Young Accounting firm needing a captivating business card

We need a business card design that forces the person to look at the card because its either gold foil, plastic, or lettering pop up etc. We already have a logo with a specific gold color and we need to make it pop. We are an accounting firm. I need the words" accounting, payroll, licenses, audits, taxes" somewhere on the business card so as to describe what we do- preferably on the side where the logo is at.

Industry/Entity Type

Accounting

Contact Information for Business Card

Address 48207 7th Ave N Ste 305, Alder Bend, OR 97117
Business Phone (503)555-0147
Fax (503)555-0193
Office Cell Phone (503)555-0162

Font styles to use
Serif

Colors
85abd2

Requirements
Must have
• It should state
• "Accounting" "Taxes" "Audits" "Licenses" "Payroll"
Nice to have
• Matte with gold foil, different textures, With Either a textured ivory background or gray blue slate background
Should not have
• colorful colors

```html
<!DOCTYPE html>
<html lang="en">
<head>
<meta charset="utf-8">
<title>NVLedgertax Business Card</title>
<link href="https://fonts.googleapis.com/css2?family=Lato:wght@400;700&display=swap" rel="stylesheet">
<style>
  :root {
    --gold: #bb9c1a;
    --gold-deep: #a88b12;
    --card-white: #ececec;
    --ink: #1e1e1e;
    --rule: #d8d2b4;
    --backdrop: #c9c9c9;
  }
  * { margin: 0; padding: 0; box-sizing: border-box; }
  html, body { width: 1200px; height: 802px; overflow: hidden; }
  body { background: var(--backdrop); font-family: "Lato", sans-serif; position: relative; }

  .card { position: absolute; top: 274px; width: 442px; height: 264px; box-shadow: 0 3px 6px rgba(0,0,0,.35); }
  .card--front { left: 136px; background: var(--card-white); }
  .card--back { left: 624px; background: var(--gold); }

  .brand { position: absolute; right: 30px; top: 100px; display: flex; align-items: center; gap: 8px; }
  .brand__mark { width: 14px; height: 14px; background: var(--gold); }
  .brand__name { font-size: 30px; font-weight: 400; color: var(--gold); letter-spacing: -0.5px; line-height: 1; }

  .person { position: absolute; left: 26px; top: 136px; }
  .person__name { font-size: 17px; font-weight: 700; color: var(--gold); letter-spacing: .2px; line-height: 1; }
  .person__title { font-size: 13px; color: var(--ink); margin-top: 2px; }
  .divider { position: absolute; left: 140px; right: 30px; top: 162px; height: 1px; background: var(--rule); }

  .contacts { position: absolute; left: 26px; top: 184px; list-style: none; }
  .contacts li { display: flex; align-items: center; gap: 5px; font-size: 13px; color: var(--ink); line-height: 15px; }
  .contacts svg { width: 11px; height: 11px; fill: var(--gold); flex: none; }

  .address { position: absolute; right: 30px; top: 208px; text-align: right; font-size: 13px; line-height: 15px; color: var(--ink); font-style: normal; }
  .band { position: absolute; left: 0; right: 0; bottom: 0; height: 10px; background: var(--gold); }

  .back-brand { position: absolute; left: 0; right: 0; top: 108px; text-align: center; font-size: 30px; font-weight: 400; color: var(--gold-deep); }
  .services { position: absolute; left: 0; right: 0; top: 222px; display: flex; justify-content: center; align-items: center; gap: 5px; list-style: none; }
  .services li { font-size: 13.5px; font-weight: 700; color: var(--ink); display: flex; align-items: center; gap: 5px; }
  .services li::before { content: ""; width: 5px; height: 5px; border-radius: 50%; background: var(--gold-deep); border: 1px solid #7d680c; }
</style>
</head>
<body>
  <section class="card card--front">
    <div class="brand">
      <span class="brand__mark"></span>
      <span class="brand__name">NVLedgertax</span>
    </div>
    <div class="person">
      <p class="person__name">DANA ELLERY</p>
      <p class="person__title">Managing Director</p>
    </div>
    <div class="divider"></div>
    <ul class="contacts">
      <li><svg viewBox="0 0 12 12"><path d="M1 4c0-2 2-3 5-3s5 1 5 3l-2 1-1-1H4L3 5zM3 6h6l1 5H2z"/></svg>(503)555-0147</li>
      <li><svg viewBox="0 0 12 12"><path d="M3 1h6v3H3zM1 5h10v4H9v2H3V9H1zM4 8v2h4V8z"/></svg>(503)555-0193</li>
      <li><svg viewBox="0 0 12 12"><path d="M3 0h6v12H3zM4 2v7h4V2z"/></svg>(503)555-0162</li>
      <li><svg viewBox="0 0 12 12"><path d="M1 3h10v7H1zM1 3l5 4 5-4"/></svg>info@samplemail.com</li>
    </ul>
    <address class="address">48207 7th Ave N Ste 305<br>Alder Bend, OR 97117</address>
    <div class="band"></div>
  </section>

  <section class="card card--back">
    <p class="back-brand">NVLedgertax</p>
    <ul class="services">
      <li>ACCOUNTING</li>
      <li>TAXES</li>
      <li>AUDITS</li>
      <li>LICENSES</li>
      <li>PAYROLL</li>
    </ul>
  </section>
</body>
</html>
```